依頼詳細
PCとスマホデザインの両方納品をいただきますが、
まずはデザインイメージが確認しやすいPCページのみの提案をお願いします。
スマホページは当選者に納品時にお願いしたいと思います。
スマホサイズについて、表示は横幅375pxで作成し、
デザインデータは2倍の横幅750pxのカンバスサイズで作成してください。
(Retinaディスプレイに対応するため)
レスポンシブウェブデザインを意識したデザインでお願いします。

■サイトマップ
添付の画面遷移図をご確認ください。

■参考サイト
http://hoshizora-tetsuko.co.jp/

■内容について
鋳造部品等を製作する会社のサイトリニューアルになります。
既存サイト
http://www.senbeiseiko.com/kiyora/index.html

■素材写真
画像データについては、フリー素材から流用して
イメージ画像に当て込んでください。
足りない場合は、一旦他のサイトの写真をサンプルとして
入れてください。(サンプルなどの表記をお願いします)
また、購入が必要な写真などを利用した場合、
価格とサイト名を教えてください。

また、Lumera Photosで定期契約をしていますので、
Lumera Photosの画像は使用できます。
デザイン時はカンプ画像をお入れいただきますようお願いします。

■ワイヤーフレーム
https://mock.wirevista.net/view/1a2b3c4d-5e6f-4a7b-8c9d-0e1f2a3b4c5d-8812/?fullscreen
コンテンツの構成としてワイヤーフレームを作成しましたが
必ずしもワイヤーフレームの通りではなくて大丈夫です。
TOPページに配置するコンテンツを見ていただき、デザインは
デザイナーの皆様におまかせしたいと思います。

----------------------------------------------------------------------------
【制作物に対するお願い】

■フォントについて
・無料で使えるフォントで作成をお願いします。
・OSに紐づくフォントの使用は控えていただければと思います (ヒラギノなど)

ページ数
1ページ
希望イメージ
シンプル 複雑
単色 カラフル
暗い 明るい
日常 高級
遊び心 厳粛
未来的 伝統的
女性的 男性的
希望する色
アクセントカラー:茶色、もしくは青色
納品ファイル
• 高解像度JPG (.jpg)
• イラストレーター形式 (.ai)
• フォトショップ形式 (.psd)
補足説明
上記のいずれか1つ(アウトラインありとなしの2つ)と高解像度JPGを納品お願いします。
adobe XDでの納品も可能です。

```html
<!DOCTYPE html>
<html lang="ja">
<head>
<meta charset="utf-8">
<title>清良伸鋼株式会社</title>
<link href="https://fonts.googleapis.com/css2?family=Noto+Sans+JP:wght@400;500;700&family=Noto+Serif+JP:wght@500;700&family=Cormorant+Garamond:ital,wght@0,600;1,500&display=swap" rel="stylesheet">
<style>
:root{
  --blue:#2f6db5;
  --blue-soft:#5b8fcf;
  --navy:#1c3559;
  --navy-deep:#15294a;
  --ink:#26303d;
  --muted:#6b7480;
  --line:#d9dee5;
  --mist:#e9eef5;
  --white:#ffffff;
}
*{margin:0;padding:0;box-sizing:border-box}
html,body{width:1200px;height:4008px;overflow:hidden}
body{font-family:"Noto Sans JP",sans-serif;color:var(--ink);background:var(--white);position:relative}
.serif{font-family:"Noto Serif JP",serif}
.photo{position:absolute}
a{color:inherit;text-decoration:none}

/* header */
.site-header{position:absolute;top:0;left:0;width:1200px;height:88px;display:flex;align-items:center;padding-left:40px;background:var(--white);z-index:3}
.brand{display:flex;flex-direction:column;font-family:"Noto Serif JP",serif;color:var(--navy);font-weight:700;line-height:1}
.brand-name{font-size:30px;letter-spacing:1px}
.brand-sub{font-size:11px;margin-top:5px;letter-spacing:1px}
.global-nav{margin-left:auto;display:flex;align-items:center;height:100%}
.global-nav a{font-size:14px;font-weight:500;margin-right:36px;color:var(--ink)}
.global-nav .nav-contact{margin:0;width:124px;height:100%;background:var(--blue);color:#fff;display:flex;align-items:center;justify-content:center;font-size:13px}

/* hero */
.hero{position:absolute;top:88px;left:0;width:1200px;height:560px;background:var(--white);overflow:hidden}
.hero-copy{position:absolute;left:40px;top:92px;z-index:2}
.hero-title{font-size:40px;line-height:1.55;letter-spacing:4px;color:var(--navy);font-weight:700}
.hero-en{font-family:"Cormorant Garamond",serif;font-style:italic;font-size:15px;color:var(--muted);margin-top:10px}

/* shared section parts */
.tag-label{display:flex;align-items:center;gap:0;flex-direction:column;align-items:flex-start}
.label-jp{font-family:"Noto Serif JP",serif;font-size:17px;color:var(--blue);font-weight:700;letter-spacing:2px}
.label-en{display:inline-block;background:var(--blue);color:#fff;font-size:9px;letter-spacing:2px;padding:2px 10px;margin-top:4px;font-weight:500}
.section-heading{font-family:"Noto Serif JP",serif;font-size:28px;line-height:1.65;color:var(--navy);font-weight:700;letter-spacing:2px;margin-top:22px}
.body-text{font-size:13px;line-height:2;color:var(--ink);margin-top:20px}
.btn-more{display:flex;align-items:center;justify-content:space-between;width:210px;height:46px;background:var(--navy);color:#fff;font-size:12px;letter-spacing:2px;padding:0 22px 0 40px;margin-top:30px;font-weight:500}
.btn-more svg{width:14px;height:10px}

/* about */
.about{position:absolute;top:648px;left:0;width:1200px;height:600px}
.about-photo{left:60px;top:112px;width:500px;height:380px;background:linear-gradient(135deg,#3a3430,#8b5a2b 45%,#e9a33c 60%,#2b2c30)}
.about-body{position:absolute;left:620px;top:110px;width:500px}

/* products */
.products{position:absolute;top:1248px;left:0;width:1200px;height:760px;background:var(--white);overflow:hidden}
.products-band{position:absolute;left:0;top:0;width:1200px;height:400px}
.products-head{position:absolute;top:70px;width:100%;text-align:center}
.products-head .label-jp{font-size:30px;color:var(--white);letter-spacing:6px}
.products-head .label-en{background:var(--white);color:var(--blue);margin-top:6px}
.product-list{position:absolute;top:190px;left:40px;width:1120px;display:flex;gap:26px}
.product-card{width:356px;background:var(--white);box-shadow:0 4px 16px rgba(28,53,89,.12)}
.product-photo{position:relative;height:240px;background:linear-gradient(160deg,#f3f4f6,#b9bec5 55%,#8e949c)}
.product-body{padding:26px 26px 30px}
.product-name{font-size:15px;font-weight:700;color:var(--navy)}
.product-text{font-size:12px;line-height:1.9;margin-top:12px;color:var(--ink)}
.products .btn-more{position:absolute;left:495px;top:660px;margin:0}

/* manufacturing */
.manufacture{position:absolute;top:2008px;left:0;width:1200px;height:560px}
.manufacture-photo{left:40px;top:20px;width:560px;height:360px;background:linear-gradient(135deg,#2c2e33,#6d6a63 45%,#a7a196 70%,#3d3f44)}
.manufacture-body{position:absolute;left:660px;top:40px;width:500px}

/* recruit */
.recruit{position:absolute;top:2568px;left:0;width:1200px;height:520px;overflow:hidden}
.recruit-photo{left:0;top:0;width:1200px;height:520px;background:linear-gradient(90deg,#f4f6f9 0%,#eef2f6 38%,#b8c6d6 70%,#7e95b0 100%)}
.recruit-body{position:absolute;left:80px;top:80px;width:520px}

/* news */
.news{position:absolute;top:3088px;left:0;width:1200px;height:420px}
.news-head{position:absolute;left:100px;top:60px}
.news-list{position:absolute;left:320px;top:60px;width:760px;list-style:none}
.news-item{display:flex;gap:30px;font-size:13px;padding:20px 10px;border-bottom:1px solid var(--line)}
.news-date{color:var(--muted);width:90px}
.news .btn-more{position:absolute;left:495px;top:330px;margin:0}

/* contact */
.contact{position:absolute;top:3508px;left:0;width:1200px;height:300px;background:var(--navy)}
.contact-lead{position:absolute;top:52px;width:100%;text-align:center;color:#fff;font-size:17px;letter-spacing:2px;font-family:"Noto Serif JP",serif}
.contact-row{position:absolute;top:112px;left:170px;width:860px;display:flex;gap:40px}
.contact-tel{width:410px;height:110px;background:#fff;display:flex;align-items:center;padding-left:36px;gap:20px}
.tel-icon{width:46px;height:46px;border-radius:50%;background:var(--blue);display:flex;align-items:center;justify-content:center}
.tel-num{font-family:"Noto Serif JP",serif;font-size:30px;font-weight:700;color:var(--navy);letter-spacing:1px}
.tel-note{font-size:11px;color:var(--muted)}
.contact-mail{width:410px;height:110px;background:var(--blue);display:flex;align-items:center;justify-content:center;gap:16px;color:#fff;font-size:18px;font-weight:500;letter-spacing:2px}

/* footer */
.site-footer{position:absolute;top:3808px;left:0;width:1200px;height:200px;background:var(--navy-deep);color:#fff}
.site-footer .brand{position:absolute;left:40px;top:50px;color:#fff}
.footer-nav{position:absolute;left:340px;top:66px;display:flex;gap:44px;font-size:13px}
.footer-bottom{position:absolute;left:0;top:140px;width:1200px;border-top:1px solid rgba(255,255,255,.15);padding:20px 40px;display:flex;font-size:11px;color:rgba(255,255,255,.75)}
.footer-bottom .links{display:flex;gap:32px}
.footer-bottom small{margin-left:auto;font-size:10px}
</style>
</head>
<body>

<header class="site-header">
  <a class="brand" href="#"><span class="brand-name">KIYORA</span><span class="brand-sub">清良伸鋼株式会社</span></a>
  <nav class="global-nav">
    <a href="#">会社案内</a><a href="#">製造案内</a><a href="#">製品紹介</a><a href="#">採用情報</a>
    <a class="nav-contact" href="#">お問い合わせ</a>
  </nav>
</header>

<section class="hero">
  <svg width="1200" height="560" style="position:absolute;left:0;top:0">
    <defs>
      <linearGradient id="forge" x1="0" y1="0" x2="1" y2="1">
        <stop offset="0" stop-color="#2a3040"/><stop offset=".45" stop-color="#6b4a2c"/>
        <stop offset=".6" stop-color="#e79a3a"/><stop offset="1" stop-color="#1e2632"/>
      </linearGradient>
    </defs>
    <polygon points="330,560 560,0 1200,0 1200,420 1060,560" fill="#2f6db5" opacity=".55"/>
    <polygon points="420,520 620,0 1200,0 1200,520" fill="url(#forge)" role="img" aria-label="鍛造作業で火花が散る様子の写真"/>
    <polygon points="300,560 380,380 520,380 440,560" fill="#5b8fcf" opacity=".7"/>
  </svg>
  <div class="hero-copy">
    <h1 class="hero-title serif">鍛造技術に、<br>自信と誇りを持って</h1>
    <p class="hero-en">We have confidence and pride in our forging technology.</p>
  </div>
</section>

<section class="about">
  <div class="photo about-photo" role="img" aria-label="赤熱した金属部品を工具で扱う鍛造現場の写真"></div>
  <div class="about-body">
    <div class="tag-label"><span class="label-jp">清良伸鋼とは</span><span class="label-en">ABOUT</span></div>
    <h2 class="section-heading">モノ造りのプロとして、<br>確かな技術でお応えします。</h2>
    <p class="body-text">清良伸鋼株式会社は新潟県燕市で70年以上に渡り、製造品を製作しています。時代のニーズに応えつつ、これまで受け継がれてきた職人の技を継承し、社員全員一丸となって努力を重ね、質の高い技術・製品・サービスを常に提供します。</p>
    <a class="btn-more" href="#">READ MORE<svg viewBox="0 0 14 10"><path d="M0 5h12M8 1l4 4-4 4" stroke="#fff" fill="none" stroke-width="1.5"/></svg></a>
  </div>
</section>

<section class="products">
  <svg class="products-band" viewBox="0 0 1200 400" preserveAspectRatio="none">
    <rect width="1200" height="400" fill="#2f6db5"/>
    <polygon points="0,0 520,0 260,400 0,400" fill="#5b8fcf" opacity=".45"/>
    <polygon points="820,0 1200,0 1200,400 620,400" fill="#1c3559" opacity=".25"/>
  </svg>
  <div class="products-head"><div class="label-jp">製品紹介</div><span class="label-en">PRODUCT</span></div>
  <div class="product-list">
    <article class="product-card">
      <div class="product-photo" role="img" aria-label="金属製の機械部品の写真"></div>
      <div class="product-body"><h3 class="product-name">機械部品</h3><p class="product-text">テキストが入ります。テキストが入ります。テキストが入ります。テキストが入ります。テキストが入ります。</p></div>
    </article>
    <article class="product-card">
      <div class="product-photo" role="img" aria-label="プレス成形された電機部品の写真"></div>
      <div class="product-body"><h3 class="product-name">電機部品</h3><p class="product-text">テキストが入ります。テキストが入ります。テキストが入ります。テキストが入ります。テキストが入ります。</p></div>
    </article>
    <article class="product-card">
      <div class="product-photo" role="img" aria-label="リング状の金属部品の写真"></div>
      <div class="product-body"><h3 class="product-name">その他の部品</h3><p class="product-text">テキストが入ります。テキストが入ります。テキストが入ります。テキストが入ります。テキストが入ります。</p></div>
    </article>
  </div>
  <a class="btn-more" href="#">READ MORE<svg viewBox="0 0 14 10"><path d="M0 5h12M8 1l4 4-4 4" stroke="#fff" fill="none" stroke-width="1.5"/></svg></a>
</section>

<section class="manufacture">
  <div class="photo manufacture-photo" role="img" aria-label="工作機械で金属を加工する製造現場の写真"></div>
  <div class="manufacture-body">
    <div class="tag-label"><span class="label-jp">製造案内</span><span class="label-en">MANUFACTURING GUIDE</span></div>
    <h2 class="section-heading">充実した設備と確かな技術で、<br>お客様のご要望に応えます。</h2>
    <p class="body-text">清良伸鋼株式会社では、自動生産ラインでは困難な製造品も、これまで培ってきた技術で製品化いたします。お客様のご要望に応じて小ロット製品から大型製品まで幅広く対応いたします。</p>
    <a class="btn-more" href="#">READ MORE<svg viewBox="0 0 14 10"><path d="M0 5h12M8 1l4 4-4 4" stroke="#fff" fill="none" stroke-width="1.5"/></svg></a>
  </div>
</section>

<section class="recruit">
  <div class="photo recruit-photo" role="img" aria-label="白いヘルメットをかぶった作業員の後ろ姿の写真"></div>
  <div class="recruit-body">
    <div class="tag-label"><span class="label-jp">採用情報</span><span class="label-en">RECRUIT</span></div>
    <h2 class="section-heading">清良伸鋼ではともに働く<br>仲間を募集しています。</h2>
    <p class="body-text">清良伸鋼株式会社では、鍛造品の製作から加工、出荷まで一貫して対応しています。お客様の様々なご要望にお応えするべく、ともに働く仲間を募集しています。当社では人材育成に力を入れており、未経験者でも一から指導し、「職人」に育て上げる環境があります。</p>
    <a class="btn-more" href="#">READ MORE<svg viewBox="0 0 14 10"><path d="M0 5h12M8 1l4 4-4 4" stroke="#fff" fill="none" stroke-width="1.5"/></svg></a>
  </div>
</section>

<section class="news">
  <div class="news-head tag-label"><span class="label-jp">お知らせ</span><span class="label-en">NEWS</span></div>
  <ul class="news-list">
    <li class="news-item"><span class="news-date">2020.00.00</span><span>テキストが入りますテキストが入りますテキストが入りますテキストが入ります</span></li>
    <li class="news-item"><span class="news-date">2020.00.00</span><span>テキストが入りますテキストが入りますテキストが入りますテキストが入ります</span></li>
    <li class="news-item"><span class="news-date">2020.00.00</span><span>テキストが入りますテキストが入りますテキストが入りますテキストが入ります</span></li>
  </ul>
  <a class="btn-more" href="#">READ MORE<svg viewBox="0 0 14 10"><path d="M0 5h12M8 1l4 4-4 4" stroke="#fff" fill="none" stroke-width="1.5"/></svg></a>
</section>

<section class="contact">
  <p class="contact-lead">ご質問やご相談を承ります。どうぞ、お気軽にお問い合わせください。</p>
  <div class="contact-row">
    <div class="contact-tel">
      <span class="tel-icon"><svg width="22" height="22" viewBox="0 0 24 24"><path d="M6.6 10.8a15.1 15.1 0 0 0 6.6 6.6l2.2-2.2c.3-.3.7-.4 1-.2 1.1.4 2.3.6 3.6.6.6 0 1 .4 1 1V20c0 .6-.4 1-1 1A17 17 0 0 1 3 4c0-.6.4-1 1-1h3.5c.6 0 1 .4 1 1 0 1.3.2 2.5.6 3.6.1.3 0 .7-.2 1z" fill="#fff"/></svg></span>
      <div><div class="tel-num">0256-77-3019</div><div class="tel-note">受付時間：8:00〜17:00（土日祝休み）</div></div>
    </div>
    <a class="contact-mail" href="#"><svg width="24" height="18" viewBox="0 0 24 18"><rect x="1" y="1" width="22" height="16" fill="none" stroke="#fff" stroke-width="1.5"/><path d="M1 1l11 9 11-9" fill="none" stroke="#fff" stroke-width="1.5"/></svg>お問い合わせ</a>
  </div>
</section>

<footer class="site-footer">
  <a class="brand" href="#"><span class="brand-name">KIYORA</span><span class="brand-sub">清良伸鋼株式会社</span></a>
  <nav class="footer-nav"><a href="#">トップページ</a><a href="#">会社案内</a><a href="#">製造案内</a><a href="#">製品紹介</a><a href="#">採用情報</a><a href="#">お知らせ</a><a href="#">お問い合わせ</a></nav>
  <div class="footer-bottom">
    <div class="links"><a href="#">プライバシーポリシー</a><a href="#">サイトマップ</a></div>
    <small>Kiyora Shindo Co., LTD. All Rights Reserved.</small>
  </div>
</footer>

</body>
</html>
```